TrailNorth Site Refresh - redesign to improve visitor journeys and conversions

I need my website brought to life, professional and engaging.
I can supply as much pictures as needed to create enhancing visuals. I need your team to review the website and create a list of ideas of what you need from me to bring this vision to life.
The company does 3d modeling, 3d printing with FDM and resin printers, CAD design, 3d scanning.
My website is https://qrfabworksco.example/
Please review it and give me your best.
Target Market(s)
cosplayer, filmmakers, life size prints, custom designs, redesign and scanning, large and small scale prints, replicating
Industry/Entity Type
CAD Design, Additive Manufacturing, 3D Printing, 3D Scanning
Coding
Coded - Design and coding required
Number of Pages Required
3 page
Font styles to use
Requirements
Must have
- Professional and clean look, inviting, eye grabber

```html
<!DOCTYPE html>
<html lang="en">
<head>
<meta charset="utf-8">
<title>QR Fab Works – 3D Printing, CAD &amp; Scanning</title>
<link href="https://fonts.googleapis.com/css2?family=Inter:wght@400;500;600;700;800&display=swap" rel="stylesheet">
<style>
:root{
  --backdrop:#b3b3b3;
  --page:#ffffff;
  --ink:#111111;
  --ink-soft:#333333;
  --dark:#121212;
  --blue:#1a9bff;
  --cyan:#2de3f5;
  --card:#f2f2f2;
  --light-band:#f4f6f8;
}
*{box-sizing:border-box;margin:0;padding:0}
html,body{width:1200px;height:2628px;overflow:hidden;background:var(--backdrop);font-family:'Inter',sans-serif;color:var(--ink)}
.page{position:absolute;left:82px;top:75px;width:1038px;height:2473px;background:var(--page);overflow:hidden;box-shadow:0 4px 18px rgba(0,0,0,.25)}
.abs{position:absolute}
.top-rule{left:0;top:0;width:100%;height:5px;background:linear-gradient(90deg,var(--blue),var(--cyan));z-index:3}

/* hero */
.hero-photo{left:0;top:5px;width:1038px;height:552px;background:linear-gradient(100deg,#1b1d20 0%,#3a3f44 35%,#6b6f70 60%,#a49a8c 80%,#7d8388 100%)}
.hero-photo::after{content:"";position:absolute;inset:0;background:radial-gradient(circle at 35% 85%,rgba(255,130,30,.45),transparent 30%),radial-gradient(circle at 25% 90%,rgba(30,160,220,.35),transparent 25%),linear-gradient(90deg,rgba(0,0,0,.55),rgba(0,0,0,.1))}
.hero-art{left:780px;top:170px;width:258px;height:520px}
.brand{left:13px;top:15px;display:flex;align-items:center;gap:10px;color:#fff;font-weight:700;font-size:22px;z-index:2}
.brand-mark{width:40px;height:40px;border-radius:50%;background:var(--blue)}
.nav{right:16px;top:12px;display:flex;align-items:center;gap:17px;font-size:10.5px;font-weight:700;color:#fff;white-space:nowrap;z-index:2}
.nav .quote{background:var(--blue);color:var(--ink);padding:0 10px;height:28px;line-height:28px}
.hero-rule{left:138px;top:257px;width:4px;height:184px;background:var(--blue)}
.hero-title{left:152px;top:253px;font-size:35px;font-weight:800;line-height:37px;color:#fff}
.hero-text{left:152px;top:333px;width:360px;font-size:12.8px;line-height:18.5px;color:#fff}
.btn{display:flex;align-items:center;justify-content:center;font-weight:600;font-size:13.5px}
.btn-white{left:152px;top:402px;width:136px;height:40px;background:#fff;color:var(--ink)}
.btn-blue{left:299px;top:402px;width:126px;height:40px;background:linear-gradient(90deg,var(--blue),var(--cyan));color:var(--ink)}

/* services */
.section-title{width:100%;text-align:center;font-size:38px;font-weight:800}
.services-title{top:626px}
.service{width:230px;height:263px;top:699px;background:var(--card);clip-path:polygon(50% 0,100% 25%,100% 75%,50% 100%,0 75%,0 25%);display:flex;flex-direction:column;align-items:center;padding:40px 16px 0;text-align:center}
.service svg{width:42px;height:50px;margin-bottom:12px}
.service h3{font-size:15.5px;font-weight:700;line-height:18px;margin-bottom:5px}
.service p{font-size:9.5px;line-height:13.5px;color:var(--ink-soft);margin-bottom:9px}
.service .more{background:linear-gradient(90deg,var(--blue),var(--cyan));font-size:9.5px;font-weight:700;padding:6px 11px}

/* work */
.work-band{left:0;top:995px;width:1038px;height:290px}
.work-title{top:1078px;color:#fff}
.work-item{clip-path:polygon(50% 0,100% 25%,100% 75%,50% 100%,0 75%,0 25%)}

/* about */
.about-art{left:99px;top:1459px;width:398px;height:456px}
.about-title{left:536px;top:1564px;font-size:38px;font-weight:800}
.about-text{left:536px;top:1610px;width:400px;font-size:9.8px;line-height:13.7px;color:var(--ink)}
.stat{top:1670px;height:68px;display:flex;flex-direction:column;align-items:center;justify-content:center}
.stat svg,.tag svg{position:absolute;inset:0;width:100%;height:100%}
.stat b{position:relative;font-size:26px;font-weight:600;line-height:28px}
.stat span{position:relative;font-size:11px;font-weight:600}
.tag{top:1759px;height:52px;width:90px;display:flex;align-items:center;justify-content:center;text-align:center;font-size:13px;line-height:15px}
.tag span{position:relative}

/* cta */
.cta-band{left:0;top:1986px;width:1038px;height:400px;background:linear-gradient(180deg,#f6f8fa,#eef1f4)}
.cta-title{top:2042px;font-size:48px;font-weight:800}
.cta-text{top:2121px;width:100%;text-align:center;font-size:16px}
.cta-btn{left:440px;top:2166px;width:157px;height:39px;background:linear-gradient(90deg,var(--blue),var(--cyan));clip-path:polygon(8% 0,92% 0,100% 50%,92% 100%,8% 100%,0 50%);font-size:13.5px;font-weight:700}
.footer-shape{left:0;top:2258px;width:1038px;height:215px}
.footer-mark{left:493px;top:2241px;width:52px;height:52px;border-radius:50%;background:var(--blue)}
.footer-text{left:0;top:2389px;width:100%;text-align:center;color:#fff;font-size:10px;line-height:16px}
</style>
</head>
<body>
<div class="page">
  <div class="abs top-rule"></div>

  <div class="abs hero-photo" role="img" aria-label="Photo of a family working beside a 3D printer with colourful printed parts on the desk"></div>
  <svg class="abs hero-art" viewBox="0 0 258 520" role="img" aria-label="Large blue printer-head and gear illustration">
    <defs><linearGradient id="artGrad" x1="0" y1="0" x2="1" y2="1"><stop offset="0" stop-color="#ffffff"/><stop offset="1" stop-color="#dff6ff"/></linearGradient>
    <linearGradient id="artBlue" x1="0" y1="0" x2="1" y2="1"><stop offset="0" stop-color="#1a9bff"/><stop offset="1" stop-color="#2de3f5"/></linearGradient></defs>
    <polygon points="258,0 258,520 130,450 40,400 26,387 26,125" fill="url(#artGrad)"/>
    <polygon points="258,40 258,500 130,425 45,375 45,140" fill="none" stroke="url(#artBlue)" stroke-width="12"/>
    <rect x="70" y="170" width="175" height="190" fill="#9fdcff" opacity=".45"/>
  </svg>

  <div class="abs brand"><span class="brand-mark"></span>QR Fab Works</div>
  <nav class="abs nav"><span>HOME</span><span>ABOUT</span><span>SERVICES &amp; SPECS</span><span class="quote">REQUEST A QUOTE</span></nav>

  <div class="abs hero-rule"></div>
  <h1 class="abs hero-title">BRING YOUR IDEAS<br>TO LIFE IN 3D</h1>
  <p class="abs hero-text">Custom 3D printing, modelling and scanning services for cosplayers, filmmakers, engineers and makers. From tiny prototypes to life-size props, we make it real.</p>
  <div class="abs btn btn-white">Request a Quote</div>
  <div class="abs btn btn-blue">See Our Work</div>

  <h2 class="abs section-title services-title">WHAT WE DO</h2>

  <div class="abs service" style="left:60px">
    <svg viewBox="0 0 42 50" fill="none" stroke="#1a9bff" stroke-width="2.5"><path d="M4 3h24l10 10v34H4z"/><path d="M28 3v10h10"/><rect x="11" y="20" width="8" height="8"/><circle cx="27" cy="34" r="4"/><path d="M10 40l5-8 5 8z"/></svg>
    <h3>FDM &amp; Resin Printing</h3>
    <p>High-precision FDM and resin printing with layer heights down to 50 µm. Build volumes up to 400×400×400 mm in a single piece.</p>
    <span class="more">LEARN MORE</span>
  </div>
  <div class="abs service" style="left:288px">
    <svg viewBox="0 0 42 50" fill="none" stroke="#1a9bff" stroke-width="2.5"><path d="M4 3h24l10 10v34H4z"/><path d="M28 3v10h10"/><path d="M14 20l5-8 5 8z"/><rect x="11" y="25" width="20" height="14"/><circle cx="21" cy="32" r="3"/></svg>
    <h3>CAD Design &amp; Modelling</h3>
    <p>We transform sketches and ideas into manufacturable CAD models, ready for printing or downstream production.</p>
    <span class="more">LEARN MORE</span>
  </div>
  <div class="abs service" style="left:517px">
    <svg viewBox="0 0 42 50" fill="none" stroke="#1a9bff" stroke-width="2.5"><circle cx="21" cy="10" r="6"/><path d="M21 18v6"/><path d="M8 32l13-7 13 7-13 7z"/><path d="M8 32v8l13 7 13-7v-8"/><path d="M4 22v-6M38 22v-6"/></svg>
    <h3>3D Scanning &amp; Reverse Engineering</h3>
    <p>Capture real-world objects with handheld scanners for modification, replication or digital archiving.</p>
    <span class="more">LEARN MORE</span>
  </div>
  <div class="abs service" style="left:745px">
    <svg viewBox="0 0 42 50" fill="none" stroke="#1a9bff" stroke-width="2.5"><rect x="4" y="10" width="34" height="36" rx="4"/><rect x="12" y="3" width="18" height="10" rx="3"/><path d="M12 24h18M12 31h18M12 38h12"/></svg>
    <h3>Post-Processing &amp; Finishing</h3>
    <p>Support removal, sanding, painting, vapor smoothing, inserts and assembly to meet your desired finish and tolerance.</p>
    <span class="more">LEARN MORE</span>
  </div>

  <svg class="abs work-band" viewBox="0 0 1038 290" preserveAspectRatio="none"><polygon points="0,106 519,0 1038,106 1038,290 0,290" fill="var(--dark)"/></svg>
  <h2 class="abs section-title work-title">RECENT WORK</h2>

  <div class="abs work-item" style="left:0;top:1182px;width:170px;height:198px;background:linear-gradient(135deg,#d7cfc2,#8a7d6e)" role="img" aria-label="Printed anatomical skull model on a workbench"></div>
  <div class="abs work-item" style="left:184px;top:1167px;width:200px;height:230px;background:linear-gradient(135deg,#e9e6e3,#e2348a)" role="img" aria-label="Pink knitted-texture egg print with ears"></div>
  <div class="abs work-item" style="left:398px;top:1143px;width:241px;height:279px;background:linear-gradient(120deg,#4fb84a,#9b4fc4,#f0a35a,#dede3c)" role="img" aria-label="Row of colourful printed pickle figures"></div>
  <div class="abs work-item" style="left:652px;top:1167px;width:200px;height:230px;background:linear-gradient(135deg,#2a2a2a,#f4c7c7,#a8d8f0,#f2e38a,#2a2a2a)" role="img" aria-label="Rainbow spiral egg print"></div>
  <div class="abs work-item" style="left:866px;top:1182px;width:172px;height:198px;background:linear-gradient(135deg,#c9b9b0,#f3efea,#d98aa0)" role="img" aria-label="Tiered cake with printed cake topper"></div>

  <svg class="abs about-art" viewBox="0 0 398 456" role="img" aria-label="Printed candlestick character and painted action figure on a rock base">
    <defs>
      <linearGradient id="leftPhoto" x1="0" y1="0" x2="0" y2="1"><stop offset="0" stop-color="#d9d4cb"/><stop offset="1" stop-color="#b98452"/></linearGradient>
      <linearGradient id="rightPhoto" x1="0" y1="0" x2="0" y2="1"><stop offset="0" stop-color="#2b3a9c"/><stop offset=".6" stop-color="#3f50c8"/><stop offset="1" stop-color="#9c9ea3"/></linearGradient>
    </defs>
    <polygon points="195,0 195,456 0,342 0,114" fill="url(#leftPhoto)"/>
    <polygon points="203,0 398,114 398,342 203,456" fill="url(#rightPhoto)"/>
    <rect x="157" y="162" width="84" height="130" rx="8" fill="#ffffff" stroke="#1f3b73" stroke-width="4"/>
    <rect x="166" y="172" width="66" height="110" rx="4" fill="#1f3b73"/>
  </svg>

  <h2 class="abs about-title">ABOUT US</h2>
  <p class="abs about-text">We’re a family-run production shop in Harlow Falls, Connecticut focussed on service, precision and clear communication. From one-off prototypes to short-run production, we help you choose the right process and deliver on time.</p>

  <div class="abs stat" style="left:536px;width:118px"><svg viewBox="0 0 118 68" preserveAspectRatio="none"><polygon points="14,1 104,1 117,34 104,67 14,67 1,34" fill="none" stroke="#2de3f5" stroke-width="1.2"/></svg><b>3000+</b><span>Parts Printed</span></div>
  <div class="abs stat" style="left:662px;width:122px"><svg viewBox="0 0 122 68" preserveAspectRatio="none"><polygon points="14,1 108,1 121,34 108,67 14,67 1,34" fill="none" stroke="#2de3f5" stroke-width="1.2"/></svg><b>120+</b><span>Happy Clients</span></div>
  <div class="abs stat" style="left:788px;width:124px"><svg viewBox="0 0 124 68" preserveAspectRatio="none"><polygon points="14,1 110,1 123,34 110,67 14,67 1,34" fill="none" stroke="#2de3f5" stroke-width="1.2"/></svg><b>3–5 d</b><span>Typical Lead Time</span></div>

  <div class="abs tag" style="left:536px"><svg viewBox="0 0 90 52" preserveAspectRatio="none"><polygon points="12,1 78,1 89,26 78,51 12,51 1,26" fill="none" stroke="#2de3f5" stroke-width="1.2"/></svg><span>Veteran<br>Support</span></div>
  <div class="abs tag" style="left:629px"><svg viewBox="0 0 90 52" preserveAspectRatio="none"><polygon points="12,1 78,1 89,26 78,51 12,51 1,26" fill="none" stroke="#2de3f5" stroke-width="1.2"/></svg><span>Made<br>in CT</span></div>
  <div class="abs tag" style="left:722px"><svg viewBox="0 0 90 52" preserveAspectRatio="none"><polygon points="12,1 78,1 89,26 78,51 12,51 1,26" fill="none" stroke="#2de3f5" stroke-width="1.2"/></svg><span>QC Report<br>Provided</span></div>

  <div class="abs cta-band" role="img" aria-label="Faint workshop photo background"></div>
  <h2 class="abs section-title cta-title">Ready to start your project?</h2>
  <p class="abs cta-text">Upload your files and tell us about your goals. We’ll review and reply within 24–48 business hours.</p>
  <div class="abs btn cta-btn">REQUEST A QUOTE</div>

  <svg class="abs footer-shape" viewBox="0 0 1038 215" preserveAspectRatio="none"><polygon points="0,115 519,0 1038,115 1038,215 0,215" fill="var(--dark)"/></svg>
  <div class="abs footer-mark"></div>
  <div class="abs footer-text">© 2025 QR Fab Works. All rights reserved.<br>hello@qrfabworksco.example &nbsp;|&nbsp; Harlow Falls, CT – Production only<br>Licensed &amp; insured. Veteran discount: 10% on labour.</div>
</div>
</body>
</html>
```